Kelvar Systems Sdn. Bhd. - logo/ B.Card and letter head
Kelvar Systems Sdn. Bhd.
Kelvar Systems Sdn. Bhd. - logo/ B.Card and letter head - Information Technology
Creative Brief
Professional
Daniel Loh
Director
Lot B14, Second Floor, East Block Meridian Shopping Mall, Jalan Cempaka 7/3, Taman Sri Kenari, 43200 Cheras, Selangor D.E
daniel.loh@kelvarplay.com
512863 - P
The name and designation will be updated later. Please include the font type on on the design upon confirmation of the design. KVS is Information technology which is specilaise in lottery and gaming business so the designer will think a logo for us. You need to specific to the designer that you need a logo
will be updated later when everything had been finalized.

```html
<!DOCTYPE html>
<html lang="en">
<head>
<meta charset="utf-8">
<title>Kelvar Systems Sdn. Bhd. – Business Card</title>
<link href="https://fonts.googleapis.com/css2?family=Exo+2:wght@400;500;600&display=swap" rel="stylesheet">
<style>
  :root {
    --bg: #e9e9ea;
    --card-white: #ffffff;
    --card-dark: #1b1b1c;
    --card-dark-edge: #3a3a3c;
    --accent-orange: #f26a1b;
    --accent-green: #5cb82e;
    --ink: #3c3c3e;
    --ink-soft: #7a7a7c;
    --ink-light: #e6e6e6;
  }
  * { margin: 0; padding: 0; box-sizing: border-box; }
  html, body { width: 1200px; height: 886px; overflow: hidden; background: var(--bg); }
  .canvas { position: relative; width: 1200px; height: 886px; font-family: "Exo 2", sans-serif; }

  .wordmark {
    font-family: "Exo 2", sans-serif; font-weight: 500;
    white-space: nowrap; line-height: 1.2;
  }

  .showcase-wordmark { position: absolute; left: 770px; top: 122px; font-size: 24px; color: var(--ink); }

  .card {
    position: absolute; border-radius: 22px; overflow: hidden;
    box-shadow: 0 18px 40px rgba(0,0,0,.18);
  }

  .card-back {
    left: 70px; top: 70px; width: 560px; height: 336px;
    background: linear-gradient(160deg, var(--card-dark-edge) 0%, var(--card-dark) 55%);
    display: flex; align-items: center; justify-content: center;
  }
  .card-back .wordmark { font-size: 20px; color: var(--ink-light); }

  .card-front {
    left: 440px; top: 420px; width: 700px; height: 420px;
    background: var(--card-white);
  }
  .front-band {
    position: absolute; left: 0; top: 0; width: 160px; height: 100%;
    background: linear-gradient(90deg, var(--card-dark) 0%, var(--card-dark-edge) 100%);
  }
  .front-wordmark { position: absolute; left: 190px; top: 52px; font-size: 18px; color: var(--ink); }

  .contact { position: absolute; left: 300px; top: 96px; color: var(--ink); }
  .contact-name { color: var(--accent-green); font-size: 27px; font-weight: 600; line-height: 1.1; }
  .contact-role { font-size: 13px; color: var(--ink-soft); margin-top: 4px; letter-spacing: .5px; }
  .contact-address { font-style: normal; font-size: 14px; line-height: 1.45; margin-top: 20px; }
  .contact-lines { margin-top: 18px; font-size: 14px; line-height: 1.5; }
  .contact-email { margin-top: 14px; font-size: 14px; }
  .label { color: var(--accent-orange); display: inline-block; min-width: 54px; }
</style>
</head>
<body>
<main class="canvas">

  <p class="wordmark showcase-wordmark">Kelvar Systems Sdn. Bhd.</p>

  <section class="card card-back" aria-label="Business card, back">
    <p class="wordmark">Kelvar Systems Sdn. Bhd.</p>
  </section>

  <section class="card card-front" aria-label="Business card, front">
    <div class="front-band"></div>
    <p class="wordmark front-wordmark">Kelvar Systems Sdn. Bhd.</p>

    <div class="contact">
      <h1 class="contact-name">Daniel Loh</h1>
      <p class="contact-role">Director</p>
      <address class="contact-address">
        Address &nbsp;Lot B14, Second Floor,<br>
        East Block Meridian Shopping Mall,<br>
        Jalan Cempaka 7/3,<br>
        Taman Sri Kenari,<br>
        43200 Cheras,<br>
        Selangor D.E
      </address>
      <p class="contact-lines">
        <span class="label">Phone</span> 03 - 5512 8840<br>
        <span class="label">Fax</span> 03 - 5512 8846
      </p>
      <p class="contact-email"><span class="label">Email</span> daniel.loh@kelvarplay.com</p>
    </div>
  </section>

</main>
</body>
</html>
```